New boutique hotel for tourists, with hint of art deco styling

This is a new, soon to be completed, boutique hotel in Sydney. A letterhead with a logo is required. Less emphasis on the word "boutique". Perhaps the word could be screened to be lighter in colour (or print intensity). Would like a simple, clear, easy-to read, sans serif type face. The information on the letterhead is:
Mrs Perrow Boutique Hotel
418 Calloway Street,
Wrenfield, NSW, 2094
Australia
Tel: +61 2 9478-0000
mrsperrowhotel@example-mail.com
mrsperrowhotel.com.au
ABN 47 902 365 118

Target Market(s)

travellers, tourists, various ages

Industry/Entity Type

Hospitality

Contact Information for Business Card

Mrs Perrow Boutique Hotel
418 Calloway Street,
Wrenfield, NSW, 2094
Telephone: (02) 9478-0000
www.mrsperrowhotel.com.au
mrsperrowhotel@example-mail.com
ABN 47 902 365 118

Logo Text

suggest playing with the letter "B"

Font styles to use
Sans Serif

Colors
3176b5

Requirements
Must have
• ABN to be very small.
• Must be clear, easy to read and in a sans serif typeface, please!
Nice to have
• The word "Boutique" should be less intense in appearance to the rest of the name, or even "Boutique Hotel" can have less prominence than "Mrs Perrow".
Should not have
• No serif typeface. Sans serif only will be accepted.

```html
<!DOCTYPE html>
<html lang="en">
<head>
<meta charset="utf-8">
<title>Mrs Perrow Boutique Hotel — Business Card</title>
<link rel="stylesheet" href="https://fonts.googleapis.com/css2?family=Jost:wght@400&display=swap">
<style>
  :root {
    --navy: #03243f;
    --paper: #ffffff;
    --backdrop: #9c9c9c;
    --ink: #0b2a47;
    --muted: #b9c4cf;
  }
  * { margin: 0; padding: 0; box-sizing: border-box; }
  html, body {
    width: 1200px; height: 1200px; overflow: hidden;
    background: var(--backdrop);
    font-family: "Jost", sans-serif;
  }
  .card {
    position: absolute; left: 346px;
    width: 507px; height: 292px;
    overflow: hidden;
  }
  .card--front { top: 257px; background: var(--paper); }
  .card--back { top: 644px; background: var(--navy); }

  .front-band {
    position: absolute; left: 0; top: 0;
    width: 100%; height: 146px; background: var(--navy);
  }
  .hotel-name {
    position: absolute; left: 0; width: 100%;
    text-align: center; color: var(--paper);
    font-weight: 400; line-height: 1; white-space: nowrap;
  }
  .card--front .hotel-name { top: 62px; font-size: 21px; }
  .card--back .hotel-name { top: 128px; font-size: 31px; }

  .address {
    position: absolute; left: 43px; top: 171px;
    font-size: 11.5px; line-height: 15.5px; color: var(--ink);
    font-style: normal;
  }
  .contacts {
    position: absolute; left: 282px; top: 178px;
    list-style: none; font-size: 11.5px; color: var(--ink);
  }
  .contacts li {
    display: flex; align-items: center; gap: 6px;
    height: 16px; white-space: nowrap;
  }
  .contacts svg { width: 8px; height: 8px; flex: none; }
  .abn {
    position: absolute; left: 0; top: 256px; width: 100%;
    text-align: center; font-size: 11px; letter-spacing: 3.5px;
    color: var(--ink);
  }
  .back-url {
    position: absolute; left: 0; top: 243px; width: 100%;
    text-align: center; font-size: 9.5px; letter-spacing: 3.6px;
    color: var(--muted);
  }
</style>
</head>
<body>

<section class="card card--front" aria-label="Business card front">
  <div class="front-band"></div>
  <p class="hotel-name">Mrs Perrow Boutique Hotel</p>
  <address class="address">
    418 Calloway Street,<br>
    Wrenfield,<br>
    Sydney, NSW 2094<br>
    Australia
  </address>
  <ul class="contacts">
    <li>
      <svg viewBox="0 0 8 8" aria-hidden="true"><rect width="8" height="8" rx="1.6" fill="#0b2a47"/><path d="M2.3 1.8l1 1-.5.6c.3.6.8 1.1 1.4 1.4l.6-.5 1 1-.6.8C3.6 6 2 4.4 1.6 2.6z" fill="#fff"/></svg>
      +61 2 9478-0000
    </li>
    <li>
      <svg viewBox="0 0 8 8" aria-hidden="true"><rect width="8" height="8" rx="1.6" fill="#0b2a47"/><rect x="1.7" y="2.4" width="4.6" height="3.2" fill="none" stroke="#fff" stroke-width=".6"/><path d="M1.7 2.4L4 4.2l2.3-1.8" fill="none" stroke="#fff" stroke-width=".6"/></svg>
      mrsperrowhotel@example-mail.com
    </li>
    <li>
      <svg viewBox="0 0 8 8" aria-hidden="true"><rect width="8" height="8" rx="1.6" fill="#0b2a47"/><circle cx="4" cy="4" r="2.2" fill="none" stroke="#fff" stroke-width=".6"/><path d="M1.8 4h4.4M4 1.8c-1 1.2-1 3.2 0 4.4M4 1.8c1 1.2 1 3.2 0 4.4" fill="none" stroke="#fff" stroke-width=".5"/></svg>
      mrsperrowhotel.com.au
    </li>
  </ul>
  <p class="abn">ABN 47 902 365 118</p>
</section>

<section class="card card--back" aria-label="Business card back">
  <p class="hotel-name">Mrs Perrow Boutique Hotel</p>
  <p class="back-url">mrsperrowhotel.com.au</p>
</section>

</body>
</html>
```